First Aid Training business needs business card design

We would like a double sided business card designed for a first aid training business - Brindlewood First Aid. We provide first aid training and , WHS (work, health and safety) training.

The attached word document contains the key information we would like on each side of the business card.

Final design needs to be delivered in print ready format, along with the original file.

```html
<!DOCTYPE html>
<html lang="en">
<head>
<meta charset="utf-8">
<title>Brindlewood First Aid – Business Card</title>
<link rel="stylesheet" href="https://fonts.googleapis.com/css2?family=Roboto+Slab:wght@300;400;600;700&display=swap">
<style>
  :root {
    --backdrop: #d5d9cd;
    --card: #efefed;
    --ink: #333333;
    --ink-soft: #444444;
    --red: #e03238;
    --slate: #505050;
    --mark: #8a8a8a;
  }
  * { box-sizing: border-box; margin: 0; padding: 0; }
  html, body {
    width: 1200px; height: 810px; overflow: hidden;
    background: var(--backdrop);
    font-family: "Roboto Slab", Georgia, serif;
    color: var(--ink);
  }
  .canvas { position: relative; width: 1200px; height: 810px; }
  .card {
    position: absolute; left: 312px; width: 577px; height: 330px;
    background: var(--card); border-radius: 3px; overflow: hidden;
    box-shadow: 0 6px 18px rgba(0,0,0,.18);
  }
  .card--front { top: 53px; }
  .card--back { top: 430px; }

  /* front */
  .brand {
    position: absolute; top: 30px; left: 0; width: 100%;
    display: flex; align-items: center; justify-content: center; gap: 22px;
  }
  .brand__dot { width: 96px; height: 96px; border-radius: 50%; background: var(--red); flex: none; }
  .brand__name {
    font-weight: 600; color: var(--ink); line-height: 1.05;
  }
  .brand__name-main { display: block; font-size: 36px; letter-spacing: .5px; }
  .brand__name-sub { display: block; font-size: 19px; letter-spacing: 1px; margin-top: 4px; }
  .front-line {
    position: absolute; left: 0; width: 100%; text-align: center; white-space: nowrap;
  }
  .front-line--lead { top: 172px; font-size: 17px; font-weight: 700; }
  .front-line--benefits { top: 222px; font-size: 17px; font-weight: 300; color: var(--ink-soft); }
  .front-line--benefits .sep { margin: 0 10px; }
  .front-line--services { top: 275px; font-size: 17px; font-weight: 700; }

  /* back */
  .band { position: absolute; display: block; }
  .band--top { top: 0; left: 0; width: 577px; height: 56px; }
  .band--bottom { bottom: 0; left: 0; width: 577px; height: 52px; }
  .back-brand {
    position: absolute; left: 50px; top: 92px; width: 200px; text-align: center;
  }
  .back-brand__dot { width: 104px; height: 104px; border-radius: 50%; background: var(--red); margin: 0 auto 12px; }
  .back-brand__name { font-size: 15px; font-weight: 700; color: var(--ink); }
  .contact-name {
    position: absolute; left: 300px; top: 84px; font-size: 23px; font-weight: 600; color: var(--red);
    padding-bottom: 4px; border-bottom: 1px solid var(--slate); width: 162px; white-space: nowrap;
  }
  .contact-list { position: absolute; left: 310px; top: 139px; list-style: none; }
  .contact-list li {
    display: flex; align-items: center; height: 20px; margin-bottom: 12px;
    font-size: 15px; color: var(--ink-soft); white-space: nowrap;
  }
  .contact-list li:last-child { margin-top: 4px; }
  .contact-list svg { width: 15px; height: 15px; margin-right: 13px; fill: var(--ink-soft); flex: none; }
</style>
</head>
<body>
<main class="canvas">

  <section class="card card--front">
    <div class="brand">
      <span class="brand__dot"></span>
      <span class="brand__name">
        <span class="brand__name-main">BRINDLEWOOD</span>
        <span class="brand__name-sub">FIRST AID TRAINING</span>
      </span>
    </div>
    <p class="front-line front-line--lead">Onsite Training – We can come to you</p>
    <p class="front-line front-line--benefits">Time efficient<span class="sep">|</span>Cost effective<span class="sep">|</span>Minimise downtime for your team</p>
    <p class="front-line front-line--services">First Aid Training | WHS Training</p>
  </section>

  <section class="card card--back">
    <svg class="band band--top" viewBox="0 0 577 56" aria-hidden="true">
      <polygon points="0,0 375,0 333,56 0,56" fill="var(--red)"/>
    </svg>
    <svg class="band band--bottom" viewBox="0 0 577 52" aria-hidden="true">
      <polygon points="299,0 577,0 577,52 277,52" fill="var(--slate)"/>
    </svg>

    <div class="back-brand">
      <div class="back-brand__dot"></div>
      <p class="back-brand__name">Brindlewood First Aid</p>
    </div>

    <h1 class="contact-name">Daniel Hartley</h1>
    <ul class="contact-list">
      <li>
        <svg viewBox="0 0 24 24" aria-hidden="true"><path d="M6.6 10.8a15.1 15.1 0 0 0 6.6 6.6l2.2-2.2a1 1 0 0 1 1-.25 11.4 11.4 0 0 0 3.6.57 1 1 0 0 1 1 1V20a1 1 0 0 1-1 1A17 17 0 0 1 3 4a1 1 0 0 1 1-1h3.5a1 1 0 0 1 1 1c0 1.25.2 2.45.57 3.57a1 1 0 0 1-.25 1z"/></svg>
        0412 356 870
      </li>
      <li>
        <svg viewBox="0 0 24 24" aria-hidden="true"><path d="M2 5h20v2l-10 6L2 7z"/><path d="M2 9l10 6 10-6v10H2z"/></svg>
        help@brindlewoodfirstaid.com.au
      </li>
      <li>
        <svg viewBox="0 0 24 24" aria-hidden="true"><path d="M12 2a10 10 0 1 0 0 20 10 10 0 0 0 0-20zm6.9 6h-2.9a15.6 15.6 0 0 0-1.4-3.6A8 8 0 0 1 18.9 8zM12 4c.8 1.2 1.5 2.5 1.9 4h-3.8c.4-1.5 1.1-2.8 1.9-4zM4.3 14a8.2 8.2 0 0 1 0-4h3.4a16 16 0 0 0 0 4zm.8 2h2.9c.3 1.3.8 2.5 1.4 3.6A8 8 0 0 1 5.1 16zM8 8H5.1a8 8 0 0 1 4.3-3.6C8.8 5.5 8.3 6.7 8 8zm4 12c-.8-1.2-1.5-2.5-1.9-4h3.8c-.4 1.5-1.1 2.8-1.9 4zm2.3-6H9.7a14.7 14.7 0 0 1 0-4h4.6a14.7 14.7 0 0 1 0 4zm.3 5.6c.6-1.1 1.1-2.3 1.4-3.6h2.9a8 8 0 0 1-4.3 3.6zm1.7-5.6a16 16 0 0 0 0-4h3.4a8.2 8.2 0 0 1 0 4z"/></svg>
        brindlewoodfirstaid.com.au
      </li>
    </ul>
  </section>

</main>
</body>
</html>
```